Advertising flyer for proofreading business.

Hello everyone,

I need an advertising flyer for a new proofreading company in Australia.

I would like your design in be in two sizes:
- A4 (to be posted on noticeboards),
- A6 (to be printed in larger quantity to give away)
(please see the size specification file attached).

The text file is attached (Ad Text) and it contains lots of information. Please feel free to include your choice of text from the text file, but please include Poster title, and highlight 'ESL' and students discounts.

I understand that it is impossible to include the same amount of information on A6 and A4, so please feel free to chose what fits on each of them, but please keep the design similar.

I have attached our company logo, but feel free to adjust it to the poster design (feel free to change the color as well). The original logo file contains circle around it, please feel free to remove it and include only the typeset as it can be seen here: http://www.lexmarka.com.au/.

Flyers will be printed, so please see the specification file for details.

I will do my best to respond to feedback as soon as possible.

I appreciate your participation, time and help,
Best wishes,
Bartosz

Target Market(s)

Students, authors

Industry/Entity Type

Business

Colors

Designer to choose colors to be used in the design.

Requirements
Must have
• It would be good if poster is easy to spot on busy noticeboards and attract attention.
• Please keep the poster in the positive/optimistic mood, and so that it focuses on students, maybe photos of graduates(?).
• Poster title,
• Please include the list of proof-read documents as they are described in the attached text file (Ad Text).
• Please highlight students discounts and ESL.
Nice to have
• I would like to leave the creative freedom to all designers so at this point I have not adjusted the Look and Feel sliders. Please feel free to offer your own take on this.
• It would be nice if most of the text could be fit to the poster.

```html
<!DOCTYPE html>
<html lang="en">
<head>
<meta charset="utf-8">
<title>Lexmarka – Professional Proofreading Services</title>
<link href="https://fonts.googleapis.com/css2?family=Montserrat:wght@400;500;600;700;800;900&family=Source+Sans+3:wght@300;400;500&display=swap" rel="stylesheet">
<style>
  :root {
    --page-bg: #ececec;
    --ink: #0b0b0b;
    --white: #ffffff;
    --teal: #2ab99e;
    --teal-soft: rgba(42, 185, 158, 0.55);
    --key-light: #f1f1f2;
    --key-mid: #d9dadc;
    --wood-dark: #4a3426;
    --wood-mid: #6e513d;
  }
  * { box-sizing: border-box; margin: 0; padding: 0; }
  html, body { width: 1200px; height: 1200px; overflow: hidden; }
  body {
    background: var(--page-bg);
    font-family: "Montserrat", Arial, sans-serif;
    color: var(--ink);
    position: relative;
  }
  .flyer {
    position: absolute;
    left: 190px; top: 20px;
    width: 820px; height: 1160px;
    background: var(--white);
    box-shadow: 0 2px 6px rgba(0,0,0,0.12);
    overflow: hidden;
  }
  .hero-photo {
    position: absolute; left: 0; top: 0; width: 820px; height: 516px;
    background:
      linear-gradient(128deg, var(--key-light) 0%, var(--key-mid) 45%, #e6e7e9 64%, transparent 64.2%),
      linear-gradient(128deg, var(--wood-mid) 0%, var(--wood-dark) 100%);
  }
  .hero-title {
    position: absolute; left: 51px; top: 80px;
    font-weight: 900; font-size: 63px; line-height: 67px;
    letter-spacing: -0.5px; color: var(--ink);
  }
  .brand {
    position: absolute; right: 50px; top: 440px;
    display: flex; align-items: center; gap: 8px;
    font-family: "Source Sans 3", Arial, sans-serif;
    font-weight: 300; font-size: 44px; color: var(--white);
  }
  .brand-dot { width: 14px; height: 14px; border-radius: 50%; background: var(--teal); }
  .teal-edge { position: absolute; left: 0; top: 500px; width: 820px; height: 16px; background: var(--teal-soft); }
  .intro {
    position: absolute; left: 0; top: 516px; width: 820px; height: 212px;
    background: var(--teal); padding: 16px 32px 0 32px;
    font-family: "Source Sans 3", Arial, sans-serif;
  }
  .intro h2 {
    font-family: "Montserrat", Arial, sans-serif;
    font-weight: 700; font-size: 34px; letter-spacing: -1px; line-height: 40px;
  }
  .intro ul { list-style: none; margin-top: 4px; }
  .intro li {
    font-size: 20.5px; font-weight: 500; line-height: 22px;
    padding-left: 16px; text-indent: -12px; margin-bottom: 9px;
  }
  .intro li::before, .doc-list li::before, .price-list li::before { content: "• "; }
  .doc-types {
    position: absolute; left: 0; top: 728px; width: 820px; height: 115px;
    background: var(--ink); color: var(--white);
    display: flex; padding: 18px 32px 0 32px;
    font-family: "Source Sans 3", Arial, sans-serif;
  }
  .doc-types .col { width: 380px; }
  .doc-types h3 { font-family: "Montserrat", Arial, sans-serif; font-weight: 700; font-size: 18px; line-height: 22px; }
  .doc-list { list-style: none; font-size: 16px; font-weight: 300; line-height: 20px; }
  .doc-list li { padding-left: 11px; text-indent: -8px; }
  .doc-types .col-right { padding-top: 0; margin-left: 0; }
  .info {
    position: absolute; left: 0; top: 843px; width: 820px; height: 223px;
    display: flex; padding: 12px 44px 0 32px;
  }
  .info h3 { font-weight: 700; font-size: 18px; }
  .price { width: 400px; }
  .price-list { list-style: none; margin-top: 16px; padding-left: 10px; }
  .price-list li {
    font-size: 11px; line-height: 14px; letter-spacing: -0.3px;
    padding-left: 9px; text-indent: -9px; margin-bottom: 8px;
  }
  .testimonial { margin-left: 2px; width: 342px; }
  .testimonial blockquote {
    margin-top: 20px; padding-left: 14px;
    font-style: italic; font-size: 13px; line-height: 25px; letter-spacing: -0.3px;
    text-align: justify;
  }
  .testimonial .credit { margin-top: 22px; text-align: right; font-size: 12px; line-height: 15px; }
  .contact-bar {
    position: absolute; left: 0; top: 1066px; width: 820px; height: 94px;
    background: var(--ink); color: var(--white); text-align: center;
  }
  .contact-bar .cta { margin-top: 20px; font-size: 13.5px; font-weight: 500; letter-spacing: 0.6px; }
  .contact-line { margin-top: 10px; display: flex; justify-content: center; gap: 22px; font-size: 13.5px; font-weight: 500; letter-spacing: 0.3px; }
  .contact-line span { display: inline-flex; align-items: center; gap: 9px; }
  .contact-line svg { width: 16px; height: 16px; }
</style>
</head>
<body>
  <div class="flyer">
    <div class="hero-photo" role="img" aria-label="Photo of a white keyboard on a wooden desk"></div>
    <h1 class="hero-title">PROFESSIONAL<br>PROOFREADING<br>SERVICES</h1>
    <div class="brand"><span class="brand-dot"></span>Lexmarka</div>
    <div class="teal-edge"></div>

    <section class="intro">
      <h2>Professional, English-language proofreading</h2>
      <ul>
        <li>Help with English as a second language (ESL - native English speaker with English Honours degree will correct all English language errors, spelling and grammar mistakes.</li>
        <li>Includes referencing and editing for style, coherence and clarity.</li>
        <li>Fast, negotiable time-frames.</li>
      </ul>
    </section>

    <section class="doc-types">
      <div class="col">
        <h3>Types of proof-read documents:</h3>
        <ul class="doc-list">
          <li>essays / assignments / theses / resumes</li>
          <li>business correspondence / training manuals / newsletters</li>
        </ul>
      </div>
      <div class="col col-right">
        <ul class="doc-list">
          <li>advertising copy / brochures / catalogues / media releases</li>
          <li>websites / presentations / speeches</li>
          <li>novels / short stories</li>
        </ul>
      </div>
    </section>

    <section class="info">
      <div class="price">
        <h3>Price guide:</h3>
        <ul class="price-list">
          <li>Prices starting at <b>$20 per page</b>. Additional charges may apply for longer and/or more complex documents (e.g. documents requiring specialist help with English as a second language).</li>
          <li>Discounts for not-for-profit organisations and students.</li>
          <li><b>Special student discount rate: $25 per hour</b> - roughly 1000 words (4 pages) of well-written text.</li>
          <li>Package deals on documents over 50,000 words.</li>
          <li>Fast turnaround times (same day service can be provided by special arrangement).</li>
        </ul>
      </div>
      <div class="testimonial">
        <h3>Testimonial:</h3>
        <blockquote>“Hannah understood our requirements quickly and has been fantastic at delivering quality work, on time and within agreed budget. It’s a pleasure to work with her.”</blockquote>
        <p class="credit">Clare Dawson<br>Operations Manager<br>Norvale AU</p>
      </div>
    </section>

    <footer class="contact-bar">
      <p class="cta">CONTACT US FOR AN OBLIGATION-FREE QUOTE</p>
      <div class="contact-line">
        <span><svg viewBox="0 0 16 16"><circle cx="8" cy="8" r="8" fill="#fff"/><path d="M5.2 4.2l1.6-.4.9 2-1 .8c.5 1.1 1.3 1.9 2.4 2.4l.8-1 2 .9-.4 1.6c-3.2.2-6.5-3.1-6.3-6.3z" fill="#0b0b0b"/></svg>0400 217 386</span>
        <span><svg viewBox="0 0 16 16"><circle cx="8" cy="8" r="8" fill="#fff"/><rect x="4" y="5.2" width="8" height="5.6" rx="0.8" fill="#0b0b0b"/><path d="M4.3 5.6L8 8.4l3.7-2.8" stroke="#fff" stroke-width="0.8" fill="none"/></svg>proofing@lexmarka.com.au</span>
        <span>www.Lexmarka.com.au</span>
      </div>
    </footer>
  </div>
</body>
</html>
```